Stationery Design Project

I need a stationary design for our company. we are based in Houston, TX and we are called Orvane Capital. And we are wanting to brand our LedgerMendPro program, which includes our tax preparation and restoration, credit repair service. Although our business offers other programs, we are interested in mainly focusing on The LedgerMendPro program. We are looking for way to brand our ourselves and I believe that a great stationery design will help in achieving this goal. Our logo design is blue and light blue. the slogan is orange.

Industry/Entity Type

Business

Requirements
Must have
• Address: 30817 Brindle Ave. K-42
Houston, TX 77519
Tel. 832-555-0187
Fax 713-555-0143
www.orvanecapital-example.com
info@orvanecapital-example.com
Our Slogan: Confidence, Renewed!

```html
<!DOCTYPE html>
<html lang="en">
<head>
<meta charset="utf-8">
<title>Orvane Capital Stationery</title>
<link href="https://fonts.googleapis.com/css2?family=Arimo:wght@700&family=Tinos:wght@400;700&display=swap" rel="stylesheet">
<style>
  :root {
    --navy: #1c3f63;
    --navy-dark: #163452;
    --accent: #8fb3d9;
    --paper: #f4f4f2;
    --backdrop: #ebebeb;
    --rule: #9aa3ad;
    --ink-soft: #4a5866;
    --label: #b9b9b9;
    --ornament: #bcc6d1;
  }
  * { margin: 0; padding: 0; box-sizing: border-box; }
  html, body { width: 1200px; height: 907px; overflow: hidden; }
  body {
    position: relative;
    background: var(--backdrop);
    font-family: "Tinos", "Times New Roman", serif;
    color: var(--navy);
  }
  .section-label {
    position: absolute; left: 57px; top: 47px;
    font-family: "Arimo", Arial, sans-serif; font-weight: 700;
    font-size: 20px; letter-spacing: 1.5px; color: var(--label);
  }
  .sheet { position: absolute; background: var(--paper); }
  .sheet--navy { background: var(--navy); color: #fff; }

  .brand-tab {
    position: absolute; background: var(--navy); color: #fff;
    display: flex; flex-direction: column; align-items: center; justify-content: flex-end;
    text-align: center; line-height: 1.1;
  }
  .brand-mark { background: var(--accent); }
  .brand-name { font-family: "Tinos", "Times New Roman", serif; font-weight: 400; color: #fff; white-space: nowrap; }

  .ornament { position: absolute; background: var(--ornament); border-radius: 3px; }
  .sheet--navy .ornament { background: #c9d3de; }

  .slogan { position: absolute; font-weight: 400; text-transform: uppercase; white-space: nowrap; letter-spacing: .3px; }
  .rule { position: absolute; height: 2px; background: var(--rule); }
  .contact { position: absolute; color: var(--ink-soft); white-space: nowrap; text-align: center; }
  .contact b { font-weight: 700; }

  /* Letterhead */
  .letterhead { left: 248px; top: 112px; width: 334px; height: 473px; }
  .letterhead .brand-tab { left: 129px; top: 0; width: 64px; height: 78px; padding-bottom: 10px; gap: 8px; }
  .letterhead .brand-mark { width: 16px; height: 16px; }
  .letterhead .brand-name { font-size: 8px; }
  .letterhead .watermark {
    position: absolute; left: 0; right: 0; top: 248px; text-align: center;
    font-size: 22px; color: #e3e3e1;
  }
  .letterhead .ornament { left: 150px; top: 413px; width: 32px; height: 6px; }
  .letterhead .slogan { left: 0; right: 0; top: 428px; text-align: center; font-size: 10.5px; }
  .letterhead .rule { left: 17px; right: 18px; top: 443px; }
  .letterhead .contact { left: 0; right: 0; font-size: 5px; }
  .letterhead .contact--address { top: 449px; }
  .letterhead .contact--web { top: 457px; }

  /* Presentation folder */
  .folder { left: 642px; top: 92px; width: 393px; height: 497px; box-shadow: inset 6px 0 0 var(--navy-dark); }
  .folder .brand-block { position: absolute; left: 0; right: 0; top: 55px; display: flex; flex-direction: column; align-items: center; gap: 12px; }
  .folder .brand-mark { width: 32px; height: 32px; }
  .folder .brand-name { font-size: 12.5px; letter-spacing: .3px; }
  .folder .ornament { left: 185px; top: 430px; width: 38px; height: 7px; }
  .folder .slogan { left: 0; right: 0; top: 447px; text-align: center; font-size: 11.5px; color: #fff; }
  .folder .rule { left: 40px; right: 23px; top: 466px; background: #8393a6; }
  .folder .contact { left: 0; right: 0; top: 474px; font-size: 7px; color: #d4dbe3; }

  /* Business cards */
  .card-front { left: 127px; top: 628px; width: 151px; height: 85px; }
  .card-front .brand-tab { left: 54px; top: 0; width: 43px; height: 43px; padding-bottom: 5px; gap: 5px; }
  .card-front .brand-mark { width: 9px; height: 9px; }
  .card-front .brand-name { font-size: 5px; }
  .card-front .slogan { left: 0; right: 0; top: 55px; text-align: center; font-size: 5.4px; }
  .card-front .rule { left: 8px; right: 8px; top: 63px; height: 1px; }
  .card-front .contact { left: 0; right: 0; font-size: 3.6px; }
  .card-front .contact--address { top: 68px; }
  .card-front .contact--web { top: 74px; }

  .card-back { left: 127px; top: 738px; width: 151px; height: 85px; }
  .card-back .brand-block { position: absolute; left: 0; right: 0; top: 20px; display: flex; flex-direction: column; align-items: center; gap: 5px; }
  .card-back .brand-mark { width: 12px; height: 12px; }
  .card-back .brand-name { font-size: 6px; }
  .card-back .contact { left: 0; right: 0; top: 64px; font-size: 5px; color: #d4dbe3; }

  /* Envelope front */
  .envelope-front { left: 318px; top: 640px; width: 374px; height: 178px; }
  .envelope-front .brand-tab { left: 23px; top: 0; width: 78px; height: 79px; padding-bottom: 11px; gap: 9px; }
  .envelope-front .brand-mark { width: 16px; height: 16px; }
  .envelope-front .brand-name { font-size: 8.5px; }
  .envelope-front .slogan { left: 22px; top: 140px; font-size: 7px; }
  .envelope-front .rule { left: 22px; right: 23px; top: 152px; }
  .envelope-front .contact { left: 22px; top: 159px; font-size: 5.5px; text-align: left; }

  /* Envelope back */
  .envelope-back { left: 728px; top: 640px; width: 374px; height: 178px; }
  .envelope-back .flap {
    position: absolute; left: 0; top: 0; width: 100%; height: 63px; background: var(--navy);
    clip-path: polygon(0 0, 100% 0, 99% 100%, 2% 100%);
    display: flex; flex-direction: column; align-items: center; justify-content: center; gap: 4px;
  }
  .envelope-back .brand-mark { width: 10px; height: 10px; }
  .envelope-back .brand-name { font-size: 6px; }
  .envelope-back .ornament { left: 172px; top: 139px; width: 30px; height: 6px; }
  .envelope-back .rule { left: 24px; right: 24px; top: 152px; height: 1px; }
  .envelope-back .slogan { left: 0; right: 0; top: 158px; text-align: center; font-size: 7.5px; color: #8e969e; }
</style>
</head>
<body>
  <div class="section-label">STATIONERY</div>

  <section class="sheet letterhead" aria-label="Letterhead">
    <div class="brand-tab"><span class="brand-mark"></span><span class="brand-name">Orvane Capital</span></div>
    <div class="watermark">Orvane Capital</div>
    <div class="ornament" role="img" aria-label="Small decorative flourish"></div>
    <div class="slogan">Orvane Capital - Confidence, Renewed!</div>
    <div class="rule"></div>
    <div class="contact contact--address">30817 Brindle Ave. K-42, Houston, TX 77519. <b>Tel:</b> 832-555-0187, <b>Fax:</b> 713-555-0143</div>
    <div class="contact contact--web">www.orvanecapital-example.com &nbsp; <b>E-mail:</b> info@orvanecapital-example.com</div>
  </section>

  <section class="sheet sheet--navy folder" aria-label="Presentation folder">
    <div class="brand-block"><span class="brand-mark"></span><span class="brand-name">Orvane Capital</span></div>
    <div class="ornament" role="img" aria-label="Small decorative flourish"></div>
    <div class="slogan">Orvane Capital - Confidence, Renewed!</div>
    <div class="rule"></div>
    <div class="contact">www.orvanecapital-example.com</div>
  </section>

  <section class="sheet card-front" aria-label="Business card front">
    <div class="brand-tab"><span class="brand-mark"></span><span class="brand-name">Orvane Capital</span></div>
    <div class="slogan">Orvane Capital - Confidence, Renewed!</div>
    <div class="rule"></div>
    <div class="contact contact--address">30817 Brindle Ave. K-42, Houston, TX 77519. <b>Tel:</b> 832-555-0187</div>
    <div class="contact contact--web"><b>Fax:</b> 713-555-0143 &nbsp; <b>E-mail:</b> info@orvanecapital-example.com</div>
  </section>

  <section class="sheet sheet--navy card-back" aria-label="Business card back">
    <div class="brand-block"><span class="brand-mark"></span><span class="brand-name">Orvane Capital</span></div>
    <div class="contact">www.orvanecapital-example.com</div>
  </section>

  <section class="sheet envelope-front" aria-label="Envelope front">
    <div class="brand-tab"><span class="brand-mark"></span><span class="brand-name">Orvane Capital</span></div>
    <div class="slogan">Orvane Capital - Confidence, Renewed!</div>
    <div class="rule"></div>
    <div class="contact">30817 Brindle Ave. K-42, Houston, TX 77519</div>
  </section>

  <section class="sheet envelope-back" aria-label="Envelope back">
    <div class="flap"><span class="brand-mark"></span><span class="brand-name">Orvane Capital</span></div>
    <div class="ornament" role="img" aria-label="Small decorative flourish"></div>
    <div class="rule"></div>
    <div class="slogan">Orvane Capital - Confidence, Renewed!</div>
  </section>
</body>
</html>
```